Kindbid mobile bidding site

Our charities can build their own event landing page to promote their silent auction fundraising event. We need a top menu, hero image with event title and desc, a register/login area, up to 4 content blocks and an auction listing of items in a grid dynamically created from their catalog. Currently we have this laid out in 100% width layers or stacks. It needs to be mobile friendly first. Examples include kpdemo.zuv.io and lindal.zuv.io and bexstest.zuv.io We need to allow people to design nice sites instead of PalNook pages that look terrible.

Target Market(s)

Soccer moms and volunteers who feel like rockstars when they learn how to use linkwave or clipvale. Not super savvy so less is more. Not overwhelming. Clean with whitespace and functional is what they want

Number of Pages Required

1 page

Font styles to use
Sans Serif

Colors

Designer to choose colors to be used in the design.

Requirements
Must have
• Nothing so tightly designed that it would look terrible if an organization loaded their own photos. This means the hero image could be landscape or portrait. When in doubt, keep it clean and simple. A one or two color palette
Nice to have
• A pop up concept for someone to log in when they choose to bid on an item in the preview.
Should not have
• Decorative fonts. Too many colors.

```html
<!DOCTYPE html>
<html lang="en">
<head>
<meta charset="utf-8">
<title>Kindbid – Event Landing Page</title>
<link rel="stylesheet" href="https://fonts.googleapis.com/css2?family=Roboto:wght@300;400;500;700;900&display=swap">
<style>
:root{
  --orange:#f7941d;
  --cyan:#1ec8d0;
  --dark:#2f2f2f;
  --ink:#222;
  --text:#666;
  --light:#f1f1f1;
  --night:#1c1c1c;
  --footer:#111;
  --white:#fff;
}
*{box-sizing:border-box;margin:0;padding:0}
html,body{width:1200px;height:3912px;overflow:hidden}
body{font-family:'Roboto',sans-serif;color:var(--text);background:var(--white);position:relative}
a{color:inherit;text-decoration:none}
ul{list-style:none}

/* ---------- Hero ---------- */
.hero{position:relative;height:620px;color:var(--white)}
.hero-photo{position:absolute;inset:0;background:linear-gradient(180deg,#141a26 0%,#2b3346 40%,#4a4038 75%,#1d1b1c 100%)}
.hero-photo::after{content:"";position:absolute;inset:0;background:rgba(0,0,0,.35)}
.topbar{position:relative;display:flex;justify-content:space-between;align-items:center;padding:10px 88px 0;font-size:12px}
.topbar .phone{display:flex;align-items:center;gap:6px;color:#ddd}
.auth{display:flex;gap:8px}
.auth a{border:1px solid var(--orange);padding:4px 12px;font-size:11px;font-weight:500;letter-spacing:.5px}
.auth a.login{background:var(--orange)}
.navbar{position:relative;display:flex;justify-content:space-between;align-items:center;padding:14px 88px}
.brand{font-size:22px;font-weight:500;color:var(--white);letter-spacing:.5px}
.menu{display:flex;gap:22px;font-size:12px;font-weight:500;letter-spacing:.6px}
.hero-copy{position:relative;text-align:center;margin-top:100px}
.hero-date{font-size:36px;font-weight:700;letter-spacing:1px}
.hero-date span{color:var(--orange)}
.hero-title{font-size:62px;font-weight:900;color:var(--orange);letter-spacing:1px;margin-top:6px}
.hero-title span{color:var(--white)}
.hero-actions{display:flex;justify-content:center;gap:18px;margin-top:26px}
.btn{display:inline-block;padding:12px 0;width:150px;text-align:center;font-size:13px;font-weight:700;letter-spacing:.5px}
.btn-orange{background:var(--orange)}
.btn-cyan{background:var(--cyan)}
.slide-arrow{position:absolute;top:262px;width:40px;height:62px;background:var(--white);display:flex;align-items:center;justify-content:center}
.slide-arrow.prev{left:0}
.slide-arrow.next{right:0}

/* ---------- Feature boxes ---------- */
.features{display:flex;gap:34px;padding:60px 88px 0;height:320px}
.feature{flex:1;height:260px;padding:34px 30px;color:var(--white)}
.feature.dark{background:var(--dark)}
.feature.orange{background:var(--orange)}
.feature.cyan{background:var(--cyan)}
.feature h3{font-size:20px;font-weight:500;margin-bottom:16px}
.feature p{font-size:13px;line-height:1.55;margin-bottom:22px}
.btn-outline{display:inline-block;border:1px solid var(--white);padding:8px 18px;font-size:11px;font-weight:500;letter-spacing:.5px}

/* ---------- Services ---------- */
.services{display:flex;justify-content:space-between;align-items:flex-start;padding:40px 88px 0;height:500px}
.services-text{width:480px;padding-top:40px}
.services-text h2{font-size:32px;font-weight:700;color:var(--ink)}
.services-text .kicker{font-size:14px;letter-spacing:1px;color:#888;margin:4px 0 22px}
.services-text p{font-size:14px;line-height:1.6;margin-bottom:14px}
.btn-line{display:inline-block;border:1px solid #444;color:#444;padding:8px 18px;font-size:11px;font-weight:500;margin-top:6px}
.devices{width:560px;height:440px;background:linear-gradient(160deg,#e9ecef,#c9ced4 60%,#aeb4bb)}

/* ---------- Auction ---------- */
.auction{padding:48px 88px 0;height:760px}
.section-head{text-align:center}
.section-head h2{font-size:28px;font-weight:700;color:var(--ink);letter-spacing:1px}
.section-head p{font-size:12px;color:#999;margin-top:4px}
.auction-body{display:flex;gap:40px;margin-top:48px}
.categories{width:200px}
.categories h4{font-size:17px;font-weight:500;color:var(--ink);margin-bottom:14px}
.categories li{display:flex;align-items:center;gap:10px;font-size:13px;padding:6px 0}
.categories li::before{content:"";width:12px;height:12px;background:#555;flex:none}
.lots{flex:1;display:grid;grid-template-columns:repeat(4,1fr);gap:26px 20px}
.lot{box-shadow:0 1px 6px rgba(0,0,0,.12);background:var(--white)}
.lot-photo{position:relative;height:196px;background:linear-gradient(160deg,#3b4050,#6b6358 60%,#2c2b2f)}
.lot-like{position:absolute;top:12px;left:12px;width:26px;height:26px;border-radius:50%;background:#e23b3b;display:flex;align-items:center;justify-content:center}
.lot-info{text-align:center;padding:10px 0 12px;font-size:11px;color:var(--ink)}
.lot-info b{display:block;font-weight:700;letter-spacing:.4px}
.lot-info span{color:var(--orange);font-weight:500}

/* ---------- FAQ ---------- */
.faq{background:var(--light);padding:56px 88px 0;height:760px}
.faq-grid{display:grid;grid-template-columns:repeat(3,1fr);gap:40px 32px;margin-top:44px}
.faq-card{background:var(--white);height:240px;padding:30px 26px}
.faq-card.active{background:var(--cyan);color:var(--white)}
.faq-card h4{font-size:15px;font-weight:700;color:var(--ink);margin-bottom:18px}
.faq-card.active h4{color:var(--white)}
.faq-card p{font-size:13px;line-height:1.55}
.faq-toggle{width:34px;height:34px;border-radius:50%;border:1px solid #bbb;margin-top:20px;display:flex;align-items:center;justify-content:center;font-size:18px;color:#777}
.faq-card.active .faq-toggle{background:var(--white);border-color:var(--white);color:var(--cyan)}

/* ---------- Testimonials ---------- */
.testimonials{background:var(--night);color:var(--white);padding:56px 0 0;height:540px}
.testimonials .section-head h2{color:var(--white)}
.quotes{display:flex;justify-content:center;gap:40px;margin-top:36px}
.quote{width:380px}
.quote-box{position:relative;background:var(--cyan);padding:26px 32px;height:180px;font-size:15px;font-weight:500;line-height:1.5}
.quote-box::after{content:"";position:absolute;left:36px;bottom:-16px;border:16px solid transparent;border-top-color:var(--cyan);border-bottom:0}
.quote-mark{font-size:40px;line-height:.6;font-weight:900;display:block;margin-bottom:10px}
.author{display:flex;align-items:center;gap:14px;margin-top:36px;font-size:14px}
.avatar{width:46px;height:46px;border-radius:50%;background:linear-gradient(160deg,#777,#444)}

/* ---------- Footer ---------- */
.footer{background:var(--footer);color:#bbb;height:432px;padding:58px 88px 0;position:relative}
.footer-cols{display:flex;gap:40px}
.footer h5{font-size:13px;font-weight:700;color:var(--cyan);letter-spacing:.5px;margin-bottom:16px}
.footer p,.footer li{font-size:12px;line-height:1.75}
.col-about{width:220px}
.col-links{width:120px}
.col-news{width:300px}
.subscribe{display:flex;height:36px}
.subscribe span{flex:1;background:var(--white);color:#999;font-size:12px;padding:10px 12px}
.subscribe b{width:40px;background:var(--orange);display:flex;align-items:center;justify-content:center}
.footer .brand{display:block;margin-top:24px;font-size:26px}
.copyright{position:absolute;left:0;right:0;bottom:30px;text-align:center;font-size:12px;color:#aaa}
.copyright span{color:var(--orange)}
</style>
</head>
<body>

<header class="hero">
  <div class="hero-photo" role="img" aria-label="Event photo of a conference hall with an audience"></div>
  <div class="topbar">
    <div class="phone">
      <svg width="12" height="12" viewBox="0 0 24 24" fill="#f7941d"><path d="M6.6 10.8a15 15 0 0 0 6.6 6.6l2.2-2.2c.3-.3.7-.4 1-.2 1.1.4 2.3.6 3.6.6.6 0 1 .4 1 1V20c0 .6-.4 1-1 1A17 17 0 0 1 3 4c0-.6.4-1 1-1h3.5c.6 0 1 .4 1 1 0 1.2.2 2.4.6 3.6.1.3 0 .7-.2 1z"/></svg>
      (000) 555 0142
    </div>
    <div class="auth"><a href="#">SIGN UP</a><a href="#" class="login">LOGIN</a></div>
  </div>
  <nav class="navbar">
    <a href="#" class="brand">Kindbid</a>
    <div class="menu">
      <a href="#">PRODUCTS</a><a href="#">PRICING</a><a href="#">OUR MISSION</a><a href="#">FAQ</a><a href="#">CONTACT</a><a href="#">BLOG</a>
    </div>
  </nav>
  <div class="hero-copy">
    <p class="hero-date"><span>20 - 22</span> JANUARY, 2020, BUFFELO CITY</p>
    <h1 class="hero-title">UX CONFERENCE <span>2020</span></h1>
    <div class="hero-actions">
      <a href="#" class="btn btn-orange">GET AUCTION</a>
      <a href="#" class="btn btn-cyan">READ MORE</a>
    </div>
  </div>
  <a href="#" class="slide-arrow prev"><svg width="12" height="18" viewBox="0 0 12 18"><path d="M10 2 3 9l7 7" stroke="#333" stroke-width="2.5" fill="none"/></svg></a>
  <a href="#" class="slide-arrow next"><svg width="12" height="18" viewBox="0 0 12 18"><path d="M2 2l7 7-7 7" stroke="#333" stroke-width="2.5" fill="none"/></svg></a>
</header>

<section class="features">
  <article class="feature dark">
    <h3>SAMPLE TEXT GOES HERE</h3>
    <p>When an unknown printer took a galley of type and scrambled it to make a type specimen book. It has survived not only five centuries.</p>
    <a href="#" class="btn-outline">READ MORE &gt;</a>
  </article>
  <article class="feature orange">
    <h3>SAMPLE TEXT GOES HERE</h3>
    <p>When an unknown printer took a galley of type and scrambled it to make a type specimen book. It has survived not only five centuries.</p>
    <a href="#" class="btn-outline">READ MORE &gt;</a>
  </article>
  <article class="feature cyan">
    <h3>SAMPLE TEXT GOES HERE</h3>
    <p>When an unknown printer took a galley of type and scrambled it to make a type specimen book. It has survived not only five centuries.</p>
    <a href="#" class="btn-outline">READ MORE &gt;</a>
  </article>
</section>

<section class="services">
  <div class="services-text">
    <h2>Industry Leading Services</h2>
    <p class="kicker">WHY IS BIDNEST BETTER?</p>
    <p>When an unknown printer took a galley of type and scrambled it to make a type specimen book. It has survived not only five centuries, but also the leap into electronic typesetting, remaining essentially unchanged. It was popularised in the 1960s with the release of Letraset sheets containing Lorem Ipsum passages, and more recently with when an unknown printer took a galley of type and scrambled it to make a type specimen book.</p>
    <a href="#" class="btn-line">READ MORE &gt;</a>
  </div>
  <div class="devices" role="img" aria-label="Laptop, tablet and phone showing the auction site"></div>
</section>

<section class="auction">
  <div class="section-head">
    <h2>AUCTION</h2>
    <p>When an unknown printer took a galley of type and scrambled it to make a type specimen book. It has survived.</p>
  </div>
  <div class="auction-body">
    <aside class="categories">
      <h4>Auction Category</h4>
      <ul>
        <li>When an unknown printer</li><li>Took a galley of type and</li><li>Scrambled it to make a type</li><li>Specimen book. It has</li><li>Survived not only five</li><li>Centuries, but also the leap</li><li>Into electronic typesetting</li><li>Remaining essentially</li><li>Unchanged. It was</li><li>Popularised in the 1960s with</li><li>The release of Letraset sheets</li><li>Containing Lorem Ipsum</li><li>Passages, and more recently</li><li>With when an unknown</li><li>printer Took a galley of type</li><li>and Scrambled it to make a</li>
      </ul>
    </aside>
    <div class="lots">
      <div class="lot"><div class="lot-photo" role="img" aria-label="Auction item photo"><span class="lot-like"><svg width="12" height="11" viewBox="0 0 24 22" fill="#fff"><path d="M12 21 2 11a6 6 0 0 1 10-7 6 6 0 0 1 10 7z"/></svg></span></div><div class="lot-info"><b>TAILING GOES HERE</b>CURRENT BID : <span>$100.00</span></div></div>
      <div class="lot"><div class="lot-photo" role="img" aria-label="Auction item photo"><span class="lot-like"><svg width="12" height="11" viewBox="0 0 24 22" fill="#fff"><path d="M12 21 2 11a6 6 0 0 1 10-7 6 6 0 0 1 10 7z"/></svg></span></div><div class="lot-info"><b>TAILING GOES HERE</b>CURRENT BID : <span>$100.00</span></div></div>
      <div class="lot"><div class="lot-photo" role="img" aria-label="Auction item photo"><span class="lot-like"><svg width="12" height="11" viewBox="0 0 24 22" fill="#fff"><path d="M12 21 2 11a6 6 0 0 1 10-7 6 6 0 0 1 10 7z"/></svg></span></div><div class="lot-info"><b>TAILING GOES HERE</b>CURRENT BID : <span>$100.00</span></div></div>
      <div class="lot"><div class="lot-photo" role="img" aria-label="Auction item photo"><span class="lot-like"><svg width="12" height="11" viewBox="0 0 24 22" fill="#fff"><path d="M12 21 2 11a6 6 0 0 1 10-7 6 6 0 0 1 10 7z"/></svg></span></div><div class="lot-info"><b>TAILING GOES HERE</b>CURRENT BID : <span>$100.00</span></div></div>
      <div class="lot"><div class="lot-photo" role="img" aria-label="Auction item photo"><span class="lot-like"><svg width="12" height="11" viewBox="0 0 24 22" fill="#fff"><path d="M12 21 2 11a6 6 0 0 1 10-7 6 6 0 0 1 10 7z"/></svg></span></div><div class="lot-info"><b>TAILING GOES HERE</b>CURRENT BID : <span>$100.00</span></div></div>
      <div class="lot"><div class="lot-photo" role="img" aria-label="Auction item photo"><span class="lot-like"><svg width="12" height="11" viewBox="0 0 24 22" fill="#fff"><path d="M12 21 2 11a6 6 0 0 1 10-7 6 6 0 0 1 10 7z"/></svg></span></div><div class="lot-info"><b>TAILING GOES HERE</b>CURRENT BID : <span>$100.00</span></div></div>
      <div class="lot"><div class="lot-photo" role="img" aria-label="Auction item photo"><span class="lot-like"><svg width="12" height="11" viewBox="0 0 24 22" fill="#fff"><path d="M12 21 2 11a6 6 0 0 1 10-7 6 6 0 0 1 10 7z"/></svg></span></div><div class="lot-info"><b>TAILING GOES HERE</b>CURRENT BID : <span>$100.00</span></div></div>
      <div class="lot"><div class="lot-photo" role="img" aria-label="Auction item photo"><span class="lot-like"><svg width="12" height="11" viewBox="0 0 24 22" fill="#fff"><path d="M12 21 2 11a6 6 0 0 1 10-7 6 6 0 0 1 10 7z"/></svg></span></div><div class="lot-info"><b>TAILING GOES HERE</b>CURRENT BID : <span>$100.00</span></div></div>
    </div>
  </div>
</section>

<section class="faq">
  <div class="section-head">
    <h2>FAQ</h2>
    <p>Need some help?</p>
  </div>
  <div class="faq-grid">
    <article class="faq-card active"><h4>When an unknown printer took ?</h4><p>Galley of type and scrambled it to make a type specimen book. It has survived not only five centuries, but also the leap into electronic typesetting, remaining.</p><span class="faq-toggle">−</span></article>
    <article class="faq-card"><h4>When an unknown printer took ?</h4><p>Galley of type and scrambled it to make a type specimen book. It has survived not only five centuries, but also the leap into electronic typesetting, remaining.</p><span class="faq-toggle">+</span></article>
    <article class="faq-card"><h4>When an unknown printer took ?</h4><p>Galley of type and scrambled it to make a type specimen book. It has survived not only five centuries, but also the leap into electronic typesetting, remaining.</p><span class="faq-toggle">+</span></article>
    <article class="faq-card"><h4>When an unknown printer took ?</h4><p>Galley of type and scrambled it to make a type specimen book. It has survived not only five centuries, but also the leap into electronic typesetting, remaining.</p><span class="faq-toggle">+</span></article>
    <article class="faq-card"><h4>When an unknown printer took ?</h4><p>Galley of type and scrambled it to make a type specimen book. It has survived not only five centuries, but also the leap into electronic typesetting, remaining.</p><span class="faq-toggle">+</span></article>
    <article class="faq-card"><h4>When an unknown printer took ?</h4><p>Galley of type and scrambled it to make a type specimen book. It has survived not only five centuries, but also the leap into electronic typesetting, remaining.</p><span class="faq-toggle">+</span></article>
  </div>
</section>

<section class="testimonials">
  <div class="section-head">
    <h2>TESTIMONIALS</h2>
    <p>See what our bidders and organisers are saying.</p>
  </div>
  <div class="quotes">
    <figure class="quote">
      <blockquote class="quote-box"><span class="quote-mark">“</span>When an unknown printer took a galley of type and scrambled it to make a type specimen book. It has survived not only five centuries, but also the leap into electronic typesetting.</blockquote>
      <figcaption class="author"><span class="avatar" role="img" aria-label="Reviewer portrait"></span>Dale Verrin</figcaption>
    </figure>
    <figure class="quote">
      <blockquote class="quote-box"><span class="quote-mark">“</span>When an unknown printer took a galley of type and scrambled it to make a type specimen book. It has survived not only five centuries, but also the leap into electronic typesetting.</blockquote>
      <figcaption class="author"><span class="avatar" role="img" aria-label="Reviewer portrait"></span>Dale Verrin</figcaption>
    </figure>
  </div>
</section>

<footer class="footer">
  <div class="footer-cols">
    <div class="col-about">
      <h5>ABOUT BIDNEST</h5>
      <p>When an unknown printer took a galley of type and scrambled it to make a type specimen book. It has survived not only five centuries, but also the leap into electronic typesetting, remaining essentially unchanged.</p>
    </div>
    <div class="col-links"><h5>NAVIGATION</h5><ul><li>Products</li><li>Pricing</li><li>Our Mission</li><li>FAQ</li><li>Contact</li><li>Blog</li></ul></div>
    <div class="col-links"><h5>OUR POLICY</h5><ul><li>Unknown printer</li><li>Took a galley of</li><li>Type and</li><li>Scrambled it to</li><li>Make a type</li><li>Specimen book</li></ul></div>
    <div class="col-links"><h5>FOLLOW US ON</h5><ul><li>Linkwave</li><li>Chirply</li><li>Workweave</li><li>Streamtube</li></ul></div>
    <div class="col-news">
      <h5>SUBSCRIBE TO OUR NEWSLETTER</h5>
      <div class="subscribe"><span>Enter your email</span><b><svg width="14" height="14" viewBox="0 0 24 24" fill="#fff"><path d="M2 21 23 12 2 3v7l15 2-15 2z"/></svg></b></div>
      <a href="#" class="brand">Kindbid</a>
    </div>
  </div>
  <p class="copyright">Copyright © 2020 <span>Kindbid</span></p>
</footer>

</body>
</html>
```